Spanish Student Needs a Cover for his PhD Dissertation

Hi everyone :) So, I'm a Corneal surgeon currently finishing my PhD, with a dissertation focused on the evaluation of quality of life in patients affected by a disease called Keratoconus. Just so you know, Keratoconus is a condition in which the cornea (the frontal part of the way) gets thin and bulgy and it decreases vision. What I did during my PhD was designing a questionnaire for evaluating quality of life in this kind of patients.
I need to design a hard cover for my dissertation, which is 200 sheets long. I like kind of minimalistic and geometric designs but I am totally open to suggestions. What needs to be in the cover is the name of the dissertation "Diseño, desarrollo y validación de una encuesta para evaluar el compromiso visual y emocional subjetivos en pacientes con Queratocono" and my name, "Iñigo Tarrasco". The other thing that needs to go there is the logo of my university (Universidad de Montebrisa). Aside from that, anything else is up to the designer. It would be important to use the kind of "red" color I am using in the dissertation. I am attaching the frontal page of my dissertation so you know what kind of design and colors I am using.
In the back part, of the cover, there should be this small inscription: "Iñigo Tarrasco, MD, es un Oftalmólogo Subespecialista en Cirugía Refractiva de la Universidad Serrana Metropolitana (Colombia) y la Universidad de Montebrisa (España). Actualmente se desempeña como miembro del Departamento de Córnea y Cirugía Refractiva de la Clínica de Oftalmología Vallealto y como director de su propia compañía de emprendimiento médico Silver Heron Surgical". Please leave a space to place my picture; I will have it taken this week so I don't have it right now, you can just leave the blank spot and I will include it later
The size of the pages is standard "letter" size.
Thanks a lot!

Target Market(s)

PhD Scholars

Font styles to use
Serif

Requirements
Must have
• The "red" color I use on my font. It must be formal but "young".
Nice to have
• I like to keep the design clean, kind of "formal with a young" touch so to speak. I really like gray colors, so it would be nice to have broad areas of gray. I love geometrical designs.
I have uploaded a very early version a friend of mine made (it even had a different title); this can be a starting point for you to work on, but I am more than open to suggestions and new ideas.
Should not have
• Please don't use my whole name, Iñigo Tarrasco is fine. I don't like ALL CAPITALS.

```html
<!DOCTYPE html>
<html lang="es">
<head>
<meta charset="UTF-8">
<title>Cubierta de tesis doctoral – Iñigo Tarrasco</title>
<link href="https://fonts.googleapis.com/css2?family=Oswald:wght@500&family=Didact+Gothic&display=swap" rel="stylesheet">
<style>
  :root {
    --crimson: #a91e3f;
    --slate: #636a63;
    --slate-dark: #4c534c;
    --photo-warm: #8a7f72;
    --paper: #ffffff;
    --ink: #1a1a1a;
  }
  html, body {
    margin: 0;
    padding: 0;
    overflow: hidden;
    background: var(--paper);
  }
  .cover {
    position: relative;
    width: 1200px;
    height: 750px;
    overflow: hidden;
    background: var(--paper);
    font-family: "Didact Gothic", sans-serif;
  }
  .front-photo {
    position: absolute;
    left: 21px;
    top: 0;
    width: 577px;
    height: 750px;
    background:
      radial-gradient(ellipse 240px 170px at 350px 470px, var(--photo-warm) 0%, rgba(138,127,114,0) 100%),
      linear-gradient(180deg, var(--slate-dark) 0%, #5d655c 50%, #474e47 100%);
  }
  .cover-shapes {
    position: absolute;
    left: 0;
    top: 0;
    width: 1200px;
    height: 750px;
  }
  .thesis-title {
    position: absolute;
    left: 63px;
    top: 104px;
    margin: 0;
    font-family: "Oswald", sans-serif;
    font-weight: 500;
    font-size: 22.5px;
    line-height: 29px;
    color: var(--paper);
    letter-spacing: 0.1px;
  }
  .author-name {
    position: absolute;
    left: 75px;
    top: 706px;
    margin: 0;
    font-size: 28px;
    line-height: 36px;
    color: var(--paper);
    font-weight: 400;
  }
  .university-mark {
    position: absolute;
    left: 429px;
    top: 0;
    width: 169px;
    height: 106px;
    background: var(--paper);
    display: flex;
    flex-direction: column;
    align-items: center;
    justify-content: flex-end;
    box-sizing: border-box;
    padding-bottom: 6px;
  }
  .university-mark .seal {
    width: 50px;
    height: 50px;
    border-radius: 50%;
    border: 1.5px solid var(--ink);
    margin-bottom: 14px;
  }
  .university-mark .rule {
    width: 100%;
    height: 1px;
    background: #999;
    margin-bottom: 4px;
  }
  .university-mark .name {
    font-size: 11.5px;
    color: var(--ink);
    white-space: nowrap;
  }
  .author-bio {
    position: absolute;
    left: 640px;
    top: 559px;
    width: 490px;
    margin: 0;
    font-size: 11.3px;
    line-height: 15px;
    color: var(--paper);
  }
</style>
</head>
<body>
<div class="cover">
  <div class="front-photo" role="img" aria-label="Fotografía: ojo que mira a través de un papel rasgado sobre madera gris"></div>

  <svg class="cover-shapes" viewBox="0 0 1600 1000" width="1200" height="750" aria-hidden="true">
    <!-- front cover -->
    <polygon points="28,0 320,0 610,212 158,445 62,935 28,1000" fill="var(--slate)"/>
    <polyline points="320,0 610,212 158,445 62,935" fill="none" stroke="#2e3a2a" stroke-width="2"/>
    <polygon points="28,0 40,0 62,935 28,1000" fill="var(--crimson)"/>
    <polygon points="28,935 430,935 525,968 430,1000 28,1000" fill="var(--crimson)"/>
    <!-- back cover -->
    <polygon points="797,0 1020,212 1345,525 1568,735 1568,1000 797,1000" fill="var(--slate)"/>
    <polygon points="1020,212 1470,2 1568,2 1568,110 1345,525" fill="var(--crimson)"/>
    <rect class="portrait-shadow" x="1007" y="232" width="324" height="308" fill="var(--crimson)" stroke="var(--paper)" stroke-width="1.5"/>
    <rect class="portrait-spot" x="1022" y="215" width="323" height="307" fill="var(--paper)"/>
  </svg>

  <div class="university-mark">
    <div class="seal"></div>
    <div class="rule"></div>
    <div class="name">Universidad de Montebrisa</div>
  </div>

  <h1 class="thesis-title">"Diseño, desarrollo y validación<br>de una encuesta para evaluar<br>el compromiso visual y emocional<br>subjetivos en pacientes<br>&nbsp;con Queratocono"</h1>

  <p class="author-name">Iñigo Tarrasco</p>

  <p class="author-bio">&nbsp;&nbsp;&nbsp;"Iñigo Tarrasco, MD, es un Oftalmólogo Subespecialista en Cirugía Refractiva de la Universidad Serrana Metropolitana (Colombia) y la Universidad de Montebrisa (España). Actualmente se desempeña como miembro del Departamento de Córnea y Cirugía Refractiva de la Clínica de Oftalmología Vallealto y como director de su propia compañía de emprendimiento médico Silver Heron Surgical "</p>
</div>
</body>
</html>
```